Pell Tor Website

Need a website that will highlight our product and provide a storefront for purchases. The design of the site (colors, logo, theme) needs to closely match the design of the product packaging and I am including files and ai file of this packaging.

Target Market(s)

Males and Females aged 16-70.

Number of Pages Required

4 page

Font styles to use
Serif

Requirements
Must have
• Home page, Product Page, Contact us page, Shop Page
• Use the general design theme that is shown in the attached AI file. Must have Pell Tor logo, must have pictures of the bugs as shown in the packaging. Can use all of the information on the ai file.
Nice to have
• Bold, clear, clean.

```html
<!DOCTYPE html>
<html lang="en">
<head>
<meta charset="utf-8">
<title>Pell Tor</title>
<link rel="stylesheet" href="https://fonts.googleapis.com/css2?family=Russo+One&family=Poppins:wght@400;500;600;700&display=swap">
<style>
:root{
  --red:#e0062b;
  --red-dark:#9c0416;
  --yellow:#f7c51c;
  --ink:#1d1d1d;
  --grey:#666;
  --footer:#222222;
  --footer-bottom:#151515;
  --white:#ffffff;
}
*{box-sizing:border-box;margin:0;padding:0}
html,body{width:1200px;height:4092px;overflow:hidden}
body{font-family:'Poppins',sans-serif;color:var(--ink);background:var(--white);position:relative}
.abs{position:absolute}
h1,h2,h3.title{font-family:'Russo One',sans-serif;font-weight:400}
.btn{display:inline-block;font-family:'Poppins',sans-serif;font-weight:600;font-size:15px;padding:12px 30px;border:0}
.btn-yellow{background:var(--yellow);color:var(--ink)}
.btn-red{background:var(--red);color:var(--white)}

/* header */
.site-header{top:0;left:0;width:1200px;height:88px;background:var(--yellow)}
.brand{top:0;left:0;width:250px;height:88px;background:var(--white);display:flex;align-items:center;justify-content:center;gap:10px;font-family:'Russo One',sans-serif;font-size:26px;color:var(--ink)}
.brand i{display:block;width:22px;height:22px;border-radius:50%;background:var(--red)}
.utility{top:0;left:250px;width:950px;height:40px;display:flex;align-items:center;justify-content:flex-end;gap:24px;padding-right:70px;font-size:14px;font-weight:500}
.utility .phone{background:var(--red);color:var(--white);padding:5px 16px;border-radius:20px;font-weight:600}
.nav{top:40px;left:250px;width:950px;height:48px;display:flex;align-items:center;justify-content:flex-end;gap:40px;padding-right:60px;font-size:14px;font-weight:600;text-transform:uppercase}
.nav .active{color:var(--red);border-bottom:2px solid var(--red);padding-bottom:2px}

/* hero */
.hero{top:88px;left:0;width:1200px;height:552px}
.hero-photo{position:absolute;inset:0;background:linear-gradient(170deg,#3d5a78 0%,#6b7f70 35%,#a0762e 65%,#c87f1e 100%)}
.hero-text{top:150px;left:92px;color:var(--white)}
.hero-text h1{font-family:'Russo One',sans-serif;font-size:64px;letter-spacing:2px}
.hero-text p{font-size:30px;font-weight:600;line-height:1.25;margin:6px 0 34px}

/* welcome */
.welcome{top:640px;left:0;width:1200px;height:448px;text-align:center}
.section-title{font-size:44px}
.section-title span{color:var(--red)}
.welcome .section-title{margin-top:72px}
.welcome p{width:900px;margin:34px auto 40px;font-size:14px;line-height:1.75;color:var(--grey)}
.welcome .btn{margin:0 10px}

/* products */
.products{top:1088px;left:0;width:1200px;height:640px;background:linear-gradient(180deg,var(--red) 0%,var(--red-dark) 100%);color:var(--white);text-align:center}
.products .section-title{margin-top:80px}
.arrow{font-family:'Poppins',sans-serif;font-size:28px;color:var(--white);top:50%}
.product{width:240px;text-align:center}
.product .name{font-weight:600;font-size:17px;margin-top:18px}
.product .price{font-size:14px}
.view-all{top:510px;left:540px}

/* protect */
.protect{top:1728px;left:0;width:1200px;height:572px}
.protect-text{top:96px;left:120px}
.protect-text h2{font-size:44px}
.protect-text h2 span{color:var(--red)}
.protect-text h3{font-size:19px;font-weight:500;margin:22px 0 14px}
.features{list-style:none;font-size:14px;color:var(--grey)}
.features li{display:flex;align-items:center;gap:12px;margin-bottom:12px}
.features li::before{content:"";width:9px;height:9px;background:var(--red)}
.protect .btn{margin-top:26px}

/* blog */
.blog{top:2300px;left:0;width:1200px;height:700px;background:linear-gradient(180deg,var(--red) 0%,var(--red-dark) 100%)}
.blog .section-title{color:var(--white);text-align:center;margin-top:80px}
.post{width:320px;height:420px;background:var(--white);top:170px}
.post-photo{height:200px}
.post-date{position:absolute;left:16px;top:160px;width:60px;height:62px;background:var(--yellow);text-align:center;font-weight:700;line-height:1.1;padding-top:8px;font-size:20px}
.post-date small{display:block;font-size:14px}
.post-body{padding:40px 20px 0}
.post-body h4{font-size:17px;font-weight:700;line-height:1.3}
.post-body p{font-size:13px;color:var(--grey);line-height:1.55;margin:10px 0 14px}
.post-body .more{font-size:13px;font-weight:700;color:var(--red)}

/* gallery */
.gallery{top:3000px;left:0;width:1200px;height:740px}
.gallery .section-title{text-align:center;margin-top:60px}
.shot{width:200px;height:220px}

/* footer */
.site-footer{top:3740px;left:0;width:1200px;height:300px;background:var(--footer);color:var(--white)}
.fcol{top:70px}
.fcol h5{font-size:22px;font-weight:500;margin-bottom:16px}
.fcol ul{list-style:none;font-size:13px;line-height:1.9;text-transform:uppercase}
.social{display:flex;gap:18px;font-size:16px;font-weight:600}
.contact li{display:flex;gap:8px;align-items:center}
.email-field{width:280px;height:44px;background:var(--footer-bottom);border:1px solid #444;font-size:13px;color:#aaa;padding:12px}
.signup{width:280px;height:44px;background:var(--yellow);color:var(--ink);font-weight:600;text-align:center;line-height:44px;margin-top:16px}
.footer-bottom{top:4040px;left:0;width:1200px;height:52px;background:var(--footer-bottom);color:#bbb;font-size:13px;display:flex;align-items:center;justify-content:space-between;padding:0 40px}
.cards{display:flex;gap:8px}
.cards span{width:40px;height:26px;background:#ddd;border-radius:3px}
</style>
</head>
<body>

<header class="site-header abs">
  <div class="brand abs"><i></i>Pell Tor</div>
  <div class="utility abs">
    <svg width="22" height="20" viewBox="0 0 22 20"><path d="M1 2h4l3 11h10l3-8H7" fill="none" stroke="#1d1d1d" stroke-width="2"/><circle cx="9" cy="17" r="1.8" fill="#1d1d1d"/><circle cx="17" cy="17" r="1.8" fill="#1d1d1d"/></svg>
    <span>My Account</span>
    <span class="phone">+0 555 010 020</span>
  </div>
  <nav class="nav abs">
    <span class="active">Home</span><span>Products</span><span>Shop</span><span>About Us</span><span>Blog</span><span>Contact Us</span>
  </nav>
</header>

<section class="hero abs">
  <div class="hero-photo" role="img" aria-label="Person wearing tall brown boots walking on autumn leaves"></div>
  <div class="hero-text abs">
    <h1>Pell Tor</h1>
    <p>Fits Child And Adult Size Non<br>Laceup Boots</p>
    <span class="btn btn-yellow">Buy Now</span>
  </div>
</section>

<section class="welcome abs">
  <h2 class="section-title">Welcome To <span>Pell Tor</span></h2>
  <p>Lorem ipsum dolor sit amet, consectetur adipiscing elit, sed do eiusmod tempor incididunt ut labore et dolore magna aliqua. Ut enim ad minim veniam, quis nostrud exercitation ullamco laboris nisi ut aliquip ex ea commodo consequat. Duis aute irure dolor in reprehenderit in voluptate velit esse cillum dolore eu fugiat nulla pariatur. Excepteur sint occaecat cupidatat non proident, sunt in culpa qui officia deserunt mollit anim id est laborum.</p>
  <span class="btn btn-red">Read More</span><span class="btn btn-yellow">Buy Now</span>
</section>

<section class="products abs">
  <h2 class="section-title">Our Products</h2>
  <span class="arrow abs" style="left:36px;top:300px">&#8249;</span>
  <span class="arrow abs" style="right:36px;top:300px">&#8250;</span>

  <div class="product abs" style="left:96px;top:170px">
    <svg width="240" height="210" viewBox="0 0 240 210"><polygon points="60,0 180,0 240,105 180,210 60,210 0,105" fill="#fff"/><rect x="70" y="35" width="100" height="140" fill="#d81d2a" role="img" aria-label="Red rain boot with black cap"/></svg>
    <div class="name">Product Name</div><div class="price">$10.00</div>
  </div>
  <div class="product abs" style="left:344px;top:170px">
    <svg width="240" height="210" viewBox="0 0 240 210"><polygon points="60,0 180,0 240,105 180,210 60,210 0,105" fill="#fff"/><rect x="70" y="35" width="100" height="140" fill="#f2c21a" role="img" aria-label="Yellow rain boot with black cap"/></svg>
    <div class="name">Product Name</div><div class="price">$10.00</div>
  </div>
  <div class="product abs" style="left:608px;top:170px">
    <svg width="240" height="210" viewBox="0 0 240 210"><polygon points="60,0 180,0 240,105 180,210 60,210 0,105" fill="#fff"/><rect x="70" y="35" width="100" height="140" fill="#c23b55" role="img" aria-label="Patterned pink boot with black cap"/></svg>
    <div class="name">Product Name</div><div class="price">$10.00</div>
  </div>
  <div class="product abs" style="left:860px;top:170px">
    <svg width="240" height="210" viewBox="0 0 240 210"><polygon points="60,0 180,0 240,105 180,210 60,210 0,105" fill="#fff"/><rect x="70" y="35" width="100" height="140" fill="#a8764a" role="img" aria-label="Brown work boot with black cap"/></svg>
    <div class="name">Product Name</div><div class="price">$10.00</div>
  </div>
  <span class="btn btn-yellow view-all abs">View All</span>
</section>

<section class="protect abs">
  <div class="protect-text abs">
    <h2>Protect <span>Yourself</span></h2>
    <h3>Package Contains One Pair(2pcs)</h3>
    <ul class="features">
      <li>Durable Poly Blend Covers</li>
      <li>Reusable</li>
      <li>One Size Fits All</li>
      <li>Machine Washable</li>
      <li>Secure Elastic Prevents Intruders</li>
    </ul>
    <span class="btn btn-yellow">Buy Now</span>
  </div>
  <svg class="abs" style="left:690px;top:90px" width="360" height="330" viewBox="0 0 360 330">
    <polygon points="90,0 270,0 360,165 270,330 90,330 0,165" fill="#e0062b"/>
    <rect x="110" y="30" width="140" height="270" fill="#c9a13a" role="img" aria-label="Boot fitted with a cap cover over its opening"/>
  </svg>
</section>

<section class="blog abs">
  <h2 class="section-title">Latest Blog</h2>
  <span class="arrow abs" style="left:36px;top:350px">&#8249;</span>
  <span class="arrow abs" style="right:36px;top:350px">&#8250;</span>

  <article class="post abs" style="left:100px">
    <div class="post-photo" role="img" aria-label="Boots on a wet wooden deck" style="background:linear-gradient(160deg,#8a7a62,#4e3b2a)"></div>
    <div class="post-date">25<small>FEB</small></div>
    <div class="post-body"><h4>Lorem ipsum dolor sit amet, consectetur adipiscing</h4><p>Lorem ipsum dolor sit amet, consect etur adipiscing elit, sed do eiusmod tempor incididunt ut labore et dolore</p><span class="more">READ MORE</span></div>
  </article>
  <article class="post abs" style="left:440px">
    <div class="post-photo" role="img" aria-label="Red boots walking on a city street" style="background:linear-gradient(160deg,#9aa2a8,#5a4a4a)"></div>
    <div class="post-date">25<small>FEB</small></div>
    <div class="post-body"><h4>Lorem ipsum dolor sit amet, consectetur adipiscing</h4><p>Lorem ipsum dolor sit amet, consect etur adipiscing elit, sed do eiusmod tempor incididunt ut labore et dolore</p><span class="more">READ MORE</span></div>
  </article>
  <article class="post abs" style="left:780px">
    <div class="post-photo" role="img" aria-label="Yellow rain boots splashing in a puddle" style="background:linear-gradient(160deg,#6c8aa0,#b59a3a)"></div>
    <div class="post-date">25<small>FEB</small></div>
    <div class="post-body"><h4>Lorem ipsum dolor sit amet, consectetur adipiscing</h4><p>Lorem ipsum dolor sit amet, consect etur adipiscing elit, sed do eiusmod tempor incididunt ut labore et dolore</p><span class="more">READ MORE</span></div>
  </article>
</section>

<section class="gallery abs">
  <h2 class="section-title">Gallery</h2>
  <div class="shot abs" style="left:270px;top:160px;background:linear-gradient(160deg,#c9b79a,#8a6a44)" role="img" aria-label="Pair of tan lace-up boots"></div>
  <div class="shot abs" style="left:480px;top:160px;background:linear-gradient(160deg,#2c8a8a,#1a1a1a)" role="img" aria-label="Black boots on a teal floor"></div>
  <div class="shot abs" style="left:690px;top:160px;background:linear-gradient(160deg,#c8c8c8,#2a2a2a)" role="img" aria-label="Black boot on a light surface"></div>
  <div class="shot abs" style="left:270px;top:400px;background:linear-gradient(160deg,#8a6a4a,#3a2a1e)" role="img" aria-label="Hiking boot on autumn ground"></div>
  <div class="shot abs" style="left:480px;top:400px;background:linear-gradient(160deg,#9aa4b0,#3a3f48)" role="img" aria-label="Boots walking on snowy pavement"></div>
  <div class="shot abs" style="left:690px;top:400px;background:linear-gradient(160deg,#d49a3a,#2a2a2a)" role="img" aria-label="Tall black boots with autumn colours"></div>
</section>

<footer class="site-footer abs">
  <div class="fcol abs" style="left:90px">
    <h5>Main menu</h5>
    <ul><li>Home</li><li>Products</li><li>Shop</li><li>About Us</li><li>Blog</li><li>Contact</li></ul>
  </div>
  <div class="fcol abs" style="left:310px">
    <h5>Stay In Touch</h5>
    <div class="social"><span>&#9679;</span><span>&#9679;</span><span>&#9679;</span><span>&#9679;</span></div>
  </div>
  <div class="fcol abs contact" style="left:560px">
    <h5>Contact Us</h5>
    <ul>
      <li>42 Harbour Row,</li>
      <li>Eastmoor</li>
      <li><svg width="12" height="12" viewBox="0 0 12 12"><path d="M2 1l3 1-1 2 4 4 2-1 1 3-2 1C5 11 1 7 1 3z" fill="#fff"/></svg>+0 555 010 020</li>
      <li><svg width="12" height="10" viewBox="0 0 12 10"><rect x="0.5" y="0.5" width="11" height="9" fill="none" stroke="#fff"/><path d="M1 1l5 4 5-4" fill="none" stroke="#fff"/></svg>info@pelltor.com</li>
    </ul>
  </div>
  <div class="fcol abs" style="left:820px">
    <h5>News &amp; updates</h5>
    <div class="email-field">Enter Your Email address</div>
    <div class="signup">Sign Up</div>
  </div>
</footer>
<div class="footer-bottom abs">
  <span>&copy; Copyrights 2020 Pell Tor. All Rights Reserved.</span>
  <div class="cards"><span></span><span></span><span></span><span></span></div>
</div>

</body>
</html>
```